Coffee bag product stickers

We currently have 4 blends of coffee (http://www.velmonbrew.com.au/ourcoffee,html) and would like to create a simple design that will be printed on clear/transparent product stickers to be placed on the front of the bags. The bags will be either black or brown so the design will need to work on both.
The design should have a consistent theme across the 4 blends with subtle differences in design or colour used to differentiate between them.
The labels we are looking at are rectangular clear poly synthetic labels, 102 x 76 mm
Information that should be incorporated in the designs is:
- our web site addresses ( www.velmonbrew.com.au )
- Name of the blend
- our logo (please see uploaded files)
Updates
Hi,
The original dimension of 100mm x 100mm have had to be altered to now be 102 mm x 76 mm. Designs do not need to fill this space completely as they will be printed on clear stickers allowing the colour of the bag to show through, however designs should also not be too small.
Many thanks.
FYI - The labels will be printed on clear label stock so the design does not need to fill the whole area and can use the colour of the bag (black - possibly brown on organic) to show through.
The idea is for it to be a sticker we place on the bag in order but for it not to look like a sticker if that make sense. It should almost be like a decal.
Thanks.
Reason: We have seen some excellent ideas and design approaches that never occurred to us while still managing to meet the brief and this is really pleasing. This has prompted us to extend the deadline to encourage more ideas for us to consider and allow us to extend our thinking even further.
Also, we felt completing the project directly after a weekend to be less than ideal.
Also, project is now a committed payment project.
Keep the ideas coming!!
Thanks,
Wallace
Colors
Designer to choose colors to be used in the design.

```html
<!DOCTYPE html>
<html lang="en">
<head>
<meta charset="utf-8">
<title>Velmon Brew – Forge Blend Label</title>
<link href="https://fonts.googleapis.com/css2?family=Cinzel:wght@400;700&family=Architects+Daughter&display=swap" rel="stylesheet">
<style>
  :root {
    --bag-black: #141414;
    --ink-white: #f4f4f4;
    --rule-grey: #8a8a8a;
    --seal-white: #ffffff;
    --seal-ink: #161616;
  }
  * { margin: 0; padding: 0; box-sizing: border-box; }
  html, body { width: 1200px; height: 1000px; overflow: hidden; background: var(--bag-black); }
  .label { position: relative; width: 1200px; height: 1000px; color: var(--ink-white); }

  .brand-name {
    position: absolute; left: 430px; top: 462px; width: 320px;
    font-family: "Cinzel", serif; font-weight: 400; font-size: 46px; line-height: 42px;
    color: var(--ink-white); text-align: center; letter-spacing: 1px;
  }
  .brand-name span { display: block; }

  .web-address {
    position: absolute; left: 478px; top: 564px; width: 216px;
    border-top: 1px solid var(--rule-grey); border-bottom: 1px solid var(--rule-grey);
    padding: 3px 0 4px;
    font-family: "Cinzel", serif; font-size: 12px; letter-spacing: 0.5px;
    text-align: center; color: var(--ink-white);
  }

  .blend-seal {
    position: absolute; left: 507px; top: 602px; width: 150px; height: 150px;
    border-radius: 50%; background: var(--seal-white); color: var(--seal-ink);
    text-align: center;
  }
  .blend-icon {
    position: absolute; left: 46px; top: 24px; width: 58px; height: 40px;
    background: var(--seal-ink); border-radius: 4px;
  }
  .blend-name {
    position: absolute; left: 0; top: 72px; width: 150px;
    font-family: "Cinzel", serif; font-weight: 700; font-size: 28px; line-height: 29px;
  }

  .details { position: absolute; left: 430px; top: 782px; width: 316px; height: 94px; }
  .details svg { position: absolute; left: 0; top: 0; }
  .field { position: absolute; }
  .field-label { font-family: "Cinzel", serif; font-size: 10px; color: var(--ink-white); }
  .field-value { font-family: "Architects Daughter", cursive; font-size: 15px; color: var(--ink-white); }
  .origin { left: 6px; top: 4px; width: 150px; }
  .origin .field-value { margin-left: 50px; }
  .use-by { left: 164px; top: 4px; width: 150px; }
  .use-by .field-value { margin-left: 20px; }
  .notes { left: 6px; top: 50px; width: 150px; }
  .notes .field-value { margin-left: 4px; }
  .weight { left: 164px; top: 50px; width: 150px; }
  .weight .field-value { margin-left: 48px; font-size: 20px; line-height: 20px; }
</style>
</head>
<body>
<main class="label">
  <h1 class="brand-name"><span>Velmon</span><span>Brew</span></h1>
  <p class="web-address">www.velmonbrew.com.au</p>

  <div class="blend-seal">
    <div class="blend-icon" role="img" aria-label="Anvil icon for the blend"></div>
    <h2 class="blend-name">Forge<br>Blend</h2>
  </div>

  <section class="details">
    <svg width="316" height="94" viewBox="0 0 316 94" aria-hidden="true">
      <line x1="0" y1="0.5" x2="316" y2="0.5" stroke="#8a8a8a" stroke-width="1.5"/>
      <line x1="0" y1="46.5" x2="316" y2="46.5" stroke="#8a8a8a" stroke-width="1.5"/>
      <line x1="0" y1="92.5" x2="316" y2="92.5" stroke="#8a8a8a" stroke-width="1.5"/>
      <line x1="158.5" y1="3" x2="158.5" y2="90" stroke="#8a8a8a" stroke-width="1.5"/>
    </svg>
    <div class="field origin"><div class="field-label">Origin</div><div class="field-value">Bolivia</div></div>
    <div class="field use-by"><div class="field-label">Use By</div><div class="field-value">04-DEC-2014</div></div>
    <div class="field notes"><div class="field-label">Notes</div><div class="field-value">Cashew, Chocolate</div></div>
    <div class="field weight"><div class="field-label">Net Weight</div><div class="field-value">250g</div></div>
  </section>
</main>
</body>
</html>
```